Brightwater Kinetics (formerly qzt7)

I'm doing a totally different business card now! I recently made some adjustments to my companies moving forward due to outstanding events. Because of this I will be increasing the prize money to the winner and second place.

Here is my new concept.

Brightwater Kinetics
Empowering futures.

My company will be in the following areas:
marketing & innovation, leadership & communication, energy & technology, culture & community, luxury & living.

I do not have a logo - so that is a must! Be creative and you will be rewarded!

I am looking for edgy, big, professional, dynamic!

One idea I had for the logo is a Brightwater symbol (needs to be created) and the shadow of words that describe my business (see above) behind it on one side and then the information on the other.

Go big - go nuts - be creative - YOU ROCK!

Target Market(s)

Multi-billion dollar corporations, world leaders, high end investors, millionaire entrepreneurs

Industry/Entity Type

Leadership

Requirements
Must have
• Name, title, phone, email, website, space for Qr code

Nice to have
• design on front and back. Possible the logo on one side and info on the other.

```html
<!DOCTYPE html>
<html lang="en">
<head>
<meta charset="utf-8">
<title>Brightwater Kinetics – Business Card</title>
<link href="https://fonts.googleapis.com/css2?family=Jost:wght@300;400;600&display=swap" rel="stylesheet">
<style>
  :root {
    --page: #ffffff;
    --frame: #8a8a8a;
    --card: #0b0b0c;
    --silver-light: #f2f2f2;
    --silver-mid: #b9b9bb;
    --silver-dark: #7d7d80;
    --text: #e6e6e6;
    --text-soft: #cfcfcf;
  }
  * { box-sizing: border-box; margin: 0; padding: 0; }
  html, body {
    width: 1200px; height: 833px; overflow: hidden;
    background: var(--page);
    font-family: "Jost", "Futura", sans-serif;
  }
  .canvas {
    position: relative; width: 1200px; height: 833px;
    border: 1px solid var(--frame);
  }
  .card {
    position: absolute; width: 539px; height: 307px;
    background: var(--card);
    border-radius: 10px; overflow: hidden;
  }
  .card::before, .card::after {
    content: ""; position: absolute; left: 0; right: 0; height: 9px;
    background: linear-gradient(90deg, var(--silver-dark) 0%, var(--silver-light) 22%, var(--silver-mid) 50%, var(--silver-light) 78%, var(--silver-dark) 100%);
  }
  .card::before { top: 0; }
  .card::after { bottom: 0; }
  .card--front { left: 212px; top: 92px; }
  .card--back { left: 436px; top: 438px; }

  .brand { position: absolute; display: flex; align-items: center; }
  .brand__mark {
    border-radius: 50%;
    background: radial-gradient(circle at 35% 30%, var(--silver-light), var(--silver-dark));
    flex: none;
  }
  .brand__name {
    color: var(--silver-light); font-weight: 600;
    text-transform: uppercase; line-height: 1.02;
  }
  .brand__tagline {
    color: var(--text-soft); font-weight: 400;
    text-transform: uppercase; letter-spacing: 0.2em;
  }
  .card--front .brand { left: 96px; top: 112px; }
  .card--front .brand__mark { width: 70px; height: 70px; margin-right: 14px; }
  .card--front .brand__name { font-size: 27px; letter-spacing: 0.04em; }
  .card--front .brand__tagline { font-size: 12px; margin-top: 8px; }

  .card--back .brand { left: 24px; top: 32px; }
  .card--back .brand__mark { width: 44px; height: 44px; margin-right: 10px; }
  .card--back .brand__name { font-size: 18px; letter-spacing: 0.04em; }
  .card--back .brand__tagline { font-size: 8.5px; margin-top: 5px; }

  .services {
    position: absolute; left: 34px; top: 104px; list-style: none;
    color: var(--text-soft); font-size: 11px; font-weight: 300; line-height: 15.4px;
  }
  .person-name {
    position: absolute; left: 363px; top: 36px;
    color: var(--text); font-size: 12.5px; font-weight: 600; letter-spacing: 0.03em;
  }
  .contact {
    position: absolute; left: 315px; top: 212px;
    color: var(--text-soft); font-size: 11.5px; font-weight: 300;
    display: grid; grid-template-columns: 77px auto; row-gap: 4.5px;
  }
  .contact dd { font-size: 10px; }
</style>
</head>
<body>
<div class="canvas">
  <section class="card card--front" aria-label="Card front">
    <div class="brand">
      <span class="brand__mark"></span>
      <div>
        <div class="brand__name">Brightwater<br>Kinetics</div>
        <div class="brand__tagline">Empowering Futures</div>
      </div>
    </div>
  </section>

  <section class="card card--back" aria-label="Card back">
    <div class="brand">
      <span class="brand__mark"></span>
      <div>
        <div class="brand__name">Brightwater<br>Kinetics</div>
        <div class="brand__tagline">Empowering Futures</div>
      </div>
    </div>
    <ul class="services">
      <li>Marketing &amp; Innovation</li>
      <li>Leadership &amp; Communication</li>
      <li>Energy &amp; Technology</li>
      <li>Culture &amp; Community</li>
      <li>Luxury &amp; Living</li>
    </ul>
    <p class="person-name">XXXXXXXXXXXXXXX</p>
    <dl class="contact">
      <dt>Toll free</dt><dd>: xxxxxxxxxxxx</dd>
      <dt>Fax</dt><dd>: xxxxxxxxxxxxxx</dd>
      <dt>Email</dt><dd>: xxxxxxxxxxxx.com</dd>
      <dt>Web</dt><dd>: www.xxxxxxxxxx.com</dd>
    </dl>
  </section>
</div>
</body>
</html>
```